Broschüre für eine Unternehmensberatung
Jonas war sehr sehr zuvorkommend und hat uns ein hervorragendes Design geliefert. Wir sind sehr dankbar für die tolle Arbeit die er geleistet hat und freuen uns auf die zukünftigen Projekte. Jonas was very forthcoming and made a great design. We really appreciate his great work and are looking forward working with him again.
Zielgruppe
Unternehmen
Wir sind eine Unternehmensberatung, die sich auf Softwareentwicklung für den Public Sektor spezialisiert hat (www.kwt-beratung.de). Wir bieten für diesen Markt verschiedene Softwareprodukte an. Eines unserer Produkte für das diese Broschüre erstellt werden soll lautet lirano (www.lirano.de) und ist eine Webapplikation die sich an Lehrer und Schüler richtet.
Company
We are a consulting company, that is specialised in softwaredevelopment regarding the public sector (www.kwt-beratung.de). Our customers are administrations all over Germany, Austria and Swiss. We offer different products to the market. Our current product is named lirano (www.lirano.de) and its targetet towards teachers and their classes.
Aufgabenstellung
Bitte keine Designs mehr einreichen, wir haben uns für einen Designer entschieden. Wir bedanken uns bei Ihnen allen für Ihre Mühe.
Die Broschüre soll hochwertig wirken und clean aussehen.
Das Produkt und die Vorteile der Nutzung sollen hervorgehoben werden (Infotext Lernverlaufsdiagnostik-v3.docx). Es muss ersichtlich werden, dass der Leherer andere Informationen bekommt als die Schüler. Wir nennen dies die Lehreransicht (Screenshot Lehrer.docx) und die Schüleransicht ( lirano Schüler - Aufgabe Lesen Klasse 2.png; lirano Schüler - Begrüßung.png; lirano Schüler - Ergebnisanzeige.png) . Es wäre gut, wenn alle Screenshots für die Schüler verwendet werden könnten.
Es sollte ein A4 Folder mit 6 Seiten werden.
Please dont send us any more designs. We found the winning one already. We thank you all for your designs and the work you put in.
The brochure should look high quality and clean.
The benefits of the product and the screenshots should be focused on((Infotext Lernverlaufsdiagnostik-v3.docx)). the brochure has to show the diffrent clients for teachers ((Screenshot Lehrer.docx)) and students ( lirano Schüler - Aufgabe Lesen Klasse 2.png; lirano Schüler - Begrüßung.png; lirano Schüler - Ergebnisanzeige.png) .
We are looking for a A4 Folder Design (6 Sites)

```html
<!DOCTYPE html>
<html lang="de">
<head>
<meta charset="utf-8">
<title>lirano – Folder</title>
<link rel="stylesheet" href="https://fonts.googleapis.com/css2?family=Lato:wght@300;400&family=Open+Sans:wght@400;600;700&display=swap">
<style>
  :root {
    --green: #9cc13f;
    --green-dark: #7fa034;
    --paper: #ffffff;
    --paper-shade: #e4e4e4;
    --text: #4a4a4a;
    --accent-red: #d3202f;
    --backdrop: #cfcfcf;
  }
  * { margin: 0; padding: 0; box-sizing: border-box; }
  html, body { width: 1200px; height: 809px; overflow: hidden; }
  body {
    background: radial-gradient(ellipse at 70% 10%, #f4f4f4 0%, var(--backdrop) 70%);
    font-family: "Open Sans", Arial, sans-serif;
    color: var(--text);
  }
  .spread {
    position: absolute; left: 105px; top: 55px;
    width: 990px; height: 700px;
    display: flex;
    box-shadow: 0 14px 34px rgba(0,0,0,.28);
  }
  .page { position: relative; width: 495px; height: 700px; overflow: hidden; }

  /* back cover */
  .back-cover { background: linear-gradient(90deg, #f1f1f1 0%, var(--paper) 45%, var(--paper-shade) 100%); }
  .back-cover .band {
    position: absolute; left: 0; right: 0; top: 120px; height: 310px;
    background: linear-gradient(90deg, #8fb83a 0%, var(--green) 50%, var(--green-dark) 100%);
  }
  .back-cover .brand-mark {
    position: absolute; left: 250px; top: 480px;
    display: flex; align-items: center; gap: 10px;
    font-weight: 700; font-size: 34px; color: var(--green);
  }
  .brand-dot { width: 22px; height: 22px; border-radius: 50%; background: var(--green); }
  .contact { position: absolute; left: 34px; bottom: 44px; }
  .contact h2 {
    font-weight: 600; font-size: 22px; color: var(--green);
    border-bottom: 1px solid var(--text); padding-bottom: 4px; width: 150px; margin-bottom: 8px;
  }
  .contact li { list-style: none; display: flex; align-items: center; gap: 8px; font-size: 12px; line-height: 20px; }
  .contact svg { width: 13px; height: 13px; }

  /* front cover */
  .front-cover { background: linear-gradient(90deg, var(--paper-shade) 0%, var(--paper) 20%, #f2f2f2 100%); }
  .front-cover .brand { position: absolute; left: 70px; top: 38px; }
  .brand-name { display: flex; align-items: center; gap: 10px; font-weight: 700; font-size: 40px; color: var(--green); line-height: 1; }
  .brand-name .brand-dot { width: 30px; height: 30px; }
  .tagline { margin: 8px 0 0 90px; font-size: 12.5px; color: var(--text); }
  .hero {
    position: absolute; left: 0; right: 0; top: 122px; height: 270px;
    background: linear-gradient(180deg, #5d6d5f 0%, #c9a98f 45%, #b98a5b 100%);
  }
  .headline {
    position: absolute; left: 60px; top: 430px;
    font-family: "Lato", Arial, sans-serif; font-weight: 300;
    font-size: 20px; line-height: 26px; letter-spacing: .5px; color: var(--green);
  }
  .partner { position: absolute; left: 60px; top: 540px; }
  .partner-name { font-weight: 700; font-size: 18px; color: var(--accent-red); }
  .partner-rule { width: 260px; height: 1px; background: var(--accent-red); margin: 2px 0 3px; }
  .partner-sub { font-size: 11px; color: var(--text); }
</style>
</head>
<body>
<main class="spread">
  <section class="page back-cover">
    <div class="band"></div>
    <div class="brand-mark"><span class="brand-dot"></span>lirano</div>
    <div class="contact">
      <h2>Kontakt</h2>
      <ul>
        <li><svg viewBox="0 0 14 14"><circle cx="7" cy="7" r="7" fill="var(--green)"/><path d="M4.5 4l1.5-.5 1 2-1 .8a5 5 0 002 2l.8-1 2 1-.5 1.5c-3 0-5.8-2.8-5.8-5.8z" fill="#fff"/></svg>+49 611 5550142</li>
        <li><svg viewBox="0 0 14 14"><circle cx="7" cy="7" r="7" fill="var(--green)"/><rect x="3.5" y="4.5" width="7" height="5" fill="#fff"/><path d="M3.5 4.5l3.5 3 3.5-3" stroke="var(--green)" fill="none" stroke-width=".8"/></svg>lernverlauf@lirano.de</li>
        <li><svg viewBox="0 0 14 14"><circle cx="7" cy="7" r="7" fill="var(--green)"/><circle cx="7" cy="7" r="3.5" fill="none" stroke="#fff" stroke-width=".8"/><path d="M3.5 7h7M7 3.5v7" stroke="#fff" stroke-width=".8"/></svg>www.lirano.de</li>
      </ul>
    </div>
  </section>

  <section class="page front-cover">
    <div class="brand">
      <div class="brand-name"><span class="brand-dot"></span>lirano.</div>
      <p class="tagline">Werkstatt für Schule und Entwicklung</p>
    </div>
    <div class="hero" role="img" aria-label="Foto: Lehrerin zeigt einer Gruppe Grundschulkinder an einem Tisch im Klassenzimmer etwas auf einem Tablet"></div>
    <h1 class="headline">FÜR LEHRER KEINE WEITERE<br>BELASTUNG LERNFORTSCHRITT<br>WIRD TRANSPARENT</h1>
    <div class="partner">
      <div class="partner-name">Kessler, Wendt &amp; Thal</div>
      <div class="partner-rule"></div>
      <div class="partner-sub">Informationssysteme GmbH</div>
    </div>
  </section>
</main>
</body>
</html>
```